Visitenkarte erstellen für Reiki Praxis

Visitenkarten für Reiki Praxis Doppelseitig

business cards reiki practice double-sided

The background can also be a different color

```html
<!DOCTYPE html>
<html lang="en">
<head>
<meta charset="utf-8">
<title>Lumen Harmony – Business Cards</title>
<link rel="stylesheet" href="https://fonts.googleapis.com/css2?family=Mulish:wght@700&family=PT+Sans:wght@400&display=swap">
<style>
  :root {
    --backdrop: #bdbdbd;
    --card-front: #fbe4ee;
    --card-back: #000000;
    --accent-rose: #b04a74;
    --accent-gold: #e2a93b;
    --ink: #111111;
    --paper-white: #ffffff;
  }
  * { margin: 0; padding: 0; box-sizing: border-box; }
  html, body {
    width: 1200px;
    height: 900px;
    overflow: hidden;
    background: var(--backdrop);
    font-family: "PT Sans", sans-serif;
  }
  .stage { position: relative; width: 1200px; height: 900px; }
  .card {
    position: absolute;
    top: 257px;
    width: 397px;
    height: 397px;
    border-radius: 28px;
    box-shadow: 4px 6px 14px rgba(0, 0, 0, 0.28);
  }
  .card--front { left: 212px; background: var(--card-front); color: var(--ink); }
  .card--back { left: 651px; background: var(--card-back); }

  .holder { position: absolute; left: 38px; top: 33px; }
  .holder__name {
    font-family: "Mulish", sans-serif;
    font-weight: 700;
    font-size: 22px;
    color: var(--accent-rose);
    line-height: 1;
  }
  .holder__role { font-size: 17px; margin-top: 5px; line-height: 1; }

  .wordmark {
    position: absolute;
    display: flex;
    flex-direction: column;
    align-items: center;
    font-family: "PT Sans", sans-serif;
    font-weight: 400;
    text-transform: uppercase;
    letter-spacing: 0.04em;
    line-height: 1.1;
  }
  .wordmark__dot {
    width: 34px; height: 34px;
    border-radius: 50%;
    margin-bottom: 14px;
  }
  .card--front .wordmark { right: 28px; top: 108px; width: 220px; color: var(--ink); font-size: 20px; }
  .card--front .wordmark__dot { background: var(--accent-rose); }
  .card--back .wordmark { left: 0; right: 0; top: 152px; color: var(--paper-white); font-size: 23px; }
  .card--back .wordmark__dot { background: var(--accent-gold); }
  .wordmark__sub { font-size: 0.7em; letter-spacing: 0.2em; }

  .contact { position: absolute; left: 35px; top: 226px; list-style: none; }
  .contact__item {
    display: flex; align-items: center;
    font-size: 17px; height: 23px;
  }
  .contact__icon { width: 14px; height: 14px; margin-right: 8px; fill: var(--accent-rose); }

  .address { position: absolute; left: 35px; top: 316px; font-size: 17px; line-height: 23px; font-style: normal; }
</style>
</head>
<body>
<main class="stage">
  <section class="card card--front">
    <div class="holder">
      <p class="holder__name">Elias Brandt</p>
      <p class="holder__role">Managing Director</p>
    </div>
    <div class="wordmark">
      <span class="wordmark__dot"></span>
      <span>Lumen Harmony</span>
      <span class="wordmark__sub">Mara Venn</span>
    </div>
    <ul class="contact">
      <li class="contact__item">
        <svg class="contact__icon" viewBox="0 0 16 16"><path d="M1 5c0-2 2-3 7-3s7 1 7 3v1h-4V5H5v1H1zM3 8l2-2h6l2 2v6H3zm5 1.5a2 2 0 100 4 2 2 0 000-4z"/></svg>
        044-987 654 321
      </li>
      <li class="contact__item">
        <svg class="contact__icon" viewBox="0 0 16 16"><path d="M1 3h14v10H1zm1.5 1.2L8 8.5l5.5-4.3v-.2h-11z"/></svg>
        hello@lumenharmony.com
      </li>
      <li class="contact__item">
        <svg class="contact__icon" viewBox="0 0 16 16"><circle cx="8" cy="8" r="7"/><path d="M1 8h14M8 1c-3 4-3 10 0 14M8 1c3 4 3 10 0 14" stroke="#fbe4ee" stroke-width="1" fill="none"/></svg>
        www.lumenharmony.com
      </li>
    </ul>
    <address class="address">Addres Line Comes Here,<br>Location Pincode 45215</address>
  </section>

  <section class="card card--back">
    <div class="wordmark">
      <span class="wordmark__dot"></span>
      <span>Lumen Harmony</span>
      <span class="wordmark__sub">Mara Venn</span>
    </div>
  </section>
</main>
</body>
</html>
```